BRAVEN VOLTWORKS SERVICES needs a vibrant design for electrical contracting work.

I require a card design for my own electrical contracting business. I will be doing a lot of domestic and commercial work, including things such as repairs, maintenance, lighting, installations and various others. LED lighting and energy efficiency will be a big part of my business. I wish not to have childish pictures such as light bulbs in the design, but rather a smart and modern looking card which incorporates my logo colours and perhaps the same lighting strike within the faded background of the card.

Target Market(s)

Residential and Commercial property owners.

Industry/Entity Type

Electrical

Contact Information for Business Card

Dario Pesek
EC40362
Phone Number: 0417 538 924
Email: dario@bravenvoltworks.com

Font styles to use
Serif
Sans Serif

Requirements
Must have
• My Logo and associated colours.
Nice to have
• Some form of shapes splitting the card into different colours related to the colours of my logo. Electric Blue, Silver/Grey and White.
Should not have
• Childish pictures and symbols such as light bulbs.

```html
<!DOCTYPE html>
<html lang="en">
<head>
<meta charset="utf-8">
<title>Braven Voltworks Services – Business Card</title>
<link rel="stylesheet" href="https://fonts.googleapis.com/css2?family=Arimo:wght@400;700&display=swap">
<style>
  :root {
    --page: #ffffff;
    --card-light: #e6e7e9;
    --electric-blue: #3a53a4;
    --steel-navy: #2c4177;
    --deep-navy: #0b2a55;
    --silver: #87888c;
    --graphite: #67686c;
    --name-navy: #0f2c5c;
    --white: #ffffff;
    --outline: #2a2a2a;
  }
  html, body {
    margin: 0;
    width: 1200px;
    height: 927px;
    overflow: hidden;
    background: var(--page);
  }
  .card {
    position: absolute;
    left: 386px;
    top: 20px;
    width: 491px;
    height: 860px;
    outline: 1px solid var(--outline);
    overflow: hidden;
    font-family: "Arimo", Arial, sans-serif;
  }
  .card__shapes { position: absolute; inset: 0; }
  .brand {
    position: absolute;
    left: 120px;
    top: 34px;
    display: flex;
    align-items: center;
    gap: 10px;
  }
  .brand__dot {
    width: 56px;
    height: 56px;
    border-radius: 50%;
    background: var(--electric-blue);
    flex: none;
  }
  .brand__name {
    color: var(--electric-blue);
    font-weight: 700;
    font-size: 23px;
    line-height: 1.15;
    letter-spacing: 0.5px;
  }
  .contact {
    position: absolute;
    left: 70px;
    top: 433px;
    color: var(--white);
  }
  .contact__name {
    margin: 0;
    color: var(--name-navy);
    font-weight: 700;
    font-size: 31px;
    letter-spacing: 0.3px;
    line-height: 1;
  }
  .contact__licence {
    margin: 6px 0 0 67px;
    font-size: 22px;
    line-height: 1;
  }
  .contact__line {
    display: flex;
    align-items: center;
    gap: 6px;
    margin: 0;
    line-height: 1;
  }
  .contact__line--phone { margin-top: 11px; font-size: 31px; }
  .contact__line--email { margin-top: 12px; font-size: 25px; }
  .contact__icon { flex: none; }
</style>
</head>
<body>
  <div class="card">
    <svg class="card__shapes" width="491" height="860" viewBox="0 0 491 860" aria-hidden="true">
      <rect width="491" height="860" fill="var(--card-light)"/>
      <polygon points="0,0 491,568 78,812 0,812" fill="var(--electric-blue)"/>
      <polygon points="0,0 78,812 0,385" fill="var(--steel-navy)"/>
      <polygon points="0,385 78,812 0,860" fill="var(--deep-navy)"/>
      <polygon points="491,568 491,620 0,860 78,812" fill="var(--silver)"/>
      <polygon points="491,620 491,860 0,860" fill="var(--graphite)"/>
    </svg>

    <div class="brand">
      <span class="brand__dot"></span>
      <span class="brand__name">BRAVEN VOLTWORKS<br>SERVICES</span>
    </div>

    <div class="contact">
      <p class="contact__name">Dario Pesek</p>
      <p class="contact__licence">EC40362</p>
      <p class="contact__line contact__line--phone">
        <svg class="contact__icon" width="24" height="24" viewBox="0 0 24 24" aria-hidden="true">
          <circle cx="12" cy="12" r="12" fill="var(--white)"/>
          <path d="M8.2 5.5l2 2.6c.3.4.2.9-.1 1.2l-1 1c.8 1.7 2 2.9 3.6 3.7l1-1c.3-.3.9-.4 1.2-.1l2.6 2c.4.3.4.9.1 1.3l-1.2 1.3c-.5.5-1.3.7-2 .4C10.6 16.6 7.4 13.4 6.1 9.7c-.3-.7-.1-1.5.4-2L7 6.4c.4-.4.9-.4 1.2-.1z" fill="var(--electric-blue)"/>
        </svg>
        0417 538 924
      </p>
      <p class="contact__line contact__line--email">
        <svg class="contact__icon" width="24" height="24" viewBox="0 0 24 24" aria-hidden="true">
          <circle cx="12" cy="12" r="12" fill="var(--white)"/>
          <rect x="6" y="8" width="12" height="8.5" rx="1" fill="var(--electric-blue)"/>
          <path d="M6.5 8.6L12 12.6l5.5-4" fill="none" stroke="var(--white)" stroke-width="1.2"/>
        </svg>
        dario@bravenvoltworks.com
      </p>
    </div>
  </div>
</body>
</html>
```